Business card for partnership

Plumbing and hvac company needing a minimal business card. We already have a logo i would like the front of the card just the logo and the back have all info.

Target Market(s)

Commercial facilities

Industry/Entity Type

Plumbing hvac

Contact Information for Business Card

We would like it double sided. Logo big and bold on the front and out info on the back. Our info on back would be name and position phone, email, and location

```html
<!DOCTYPE html>
<html lang="en">
<head>
<meta charset="utf-8">
<title>Kestrel Mechanical – Business Card</title>
<link rel="stylesheet" href="https://fonts.googleapis.com/css2?family=Arimo:wght@400;700&display=swap">
<style>
  :root {
    --stage: #2b2e33;
    --card-black: #121212;
    --card-white: #ffffff;
    --accent: #f28a2e;
    --ink: #111111;
    --ink-soft: #333333;
  }
  * { margin: 0; padding: 0; box-sizing: border-box; }
  html, body {
    width: 1200px; height: 900px; overflow: hidden;
    background: var(--stage);
    font-family: "Arimo", Arial, sans-serif;
  }
  .canvas { position: relative; width: 1200px; height: 900px; }
  .card {
    position: absolute; left: 337px;
    width: 525px; height: 300px;
    border-radius: 4px; overflow: hidden;
    box-shadow: 0 14px 30px rgba(0,0,0,.45);
  }
  /* Front */
  .card-front { top: 110px; background: var(--card-black); }
  .front-wordmark {
    position: absolute; inset: 0;
    display: flex; flex-direction: column; align-items: center; justify-content: center;
    color: var(--card-white); font-weight: 700; line-height: 1;
  }
  .front-wordmark .brand-main { font-size: 66px; letter-spacing: 2px; }
  .front-wordmark .brand-sub { font-size: 27px; letter-spacing: 7px; margin-top: 8px; }

  /* Back */
  .card-back { top: 490px; background: var(--card-white); }
  .card-back svg.back-shapes { position: absolute; inset: 0; }
  .back-wordmark {
    position: absolute; left: 84px; top: 92px;
    color: var(--ink); font-weight: 700; line-height: 1;
  }
  .back-wordmark .brand-main { font-size: 32px; letter-spacing: 1px; }
  .back-wordmark .brand-sub { font-size: 13px; letter-spacing: 3.4px; margin-top: 5px; }
  .divider {
    position: absolute; left: 256px; top: 66px;
    width: 2px; height: 135px; background: var(--accent);
  }
  .person { position: absolute; left: 276px; top: 72px; color: var(--ink); }
  .person-name { font-size: 23px; font-weight: 700; letter-spacing: .5px; white-space: nowrap; }
  .person-role { font-size: 12px; color: var(--ink-soft); margin-top: 4px; }
  .person-rule { width: 42px; height: 3px; background: var(--accent); margin-top: 8px; }
  .contact { list-style: none; margin-top: 12px; }
  .contact li {
    display: flex; align-items: center; gap: 7px;
    font-size: 12px; color: var(--ink); margin-bottom: 7px; white-space: nowrap;
  }
  .contact svg { width: 12px; height: 12px; flex: none; }
</style>
</head>
<body>
<main class="canvas">

  <section class="card card-front" aria-label="Card front">
    <div class="front-wordmark">
      <span class="brand-main">KESTREL</span>
      <span class="brand-sub">MECHANICAL</span>
    </div>
  </section>

  <section class="card card-back" aria-label="Card back">
    <svg class="back-shapes" viewBox="0 0 525 300" width="525" height="300" aria-hidden="true">
      <rect x="0" y="0" width="300" height="12" fill="var(--accent)"/>
      <rect x="300" y="0" width="225" height="12" fill="var(--card-black)"/>
      <path d="M0 12 L20 12 C 30 170 160 270 420 300 L0 300 Z" fill="var(--card-black)"/>
      <path d="M62 172 C 130 250 270 285 480 300" fill="none" stroke="var(--accent)" stroke-width="4"/>
    </svg>

    <div class="back-wordmark">
      <div class="brand-main">KESTREL</div>
      <div class="brand-sub">MECHANICAL</div>
    </div>

    <div class="divider"></div>

    <div class="person">
      <div class="person-name">DANIEL REYES</div>
      <div class="person-role">Solution Manager</div>
      <div class="person-rule"></div>
      <ul class="contact">
        <li>
          <svg viewBox="0 0 24 24"><path fill="var(--accent)" d="M6.6 10.8a15.1 15.1 0 0 0 6.6 6.6l2.2-2.2a1 1 0 0 1 1-.25 11.4 11.4 0 0 0 3.6.57 1 1 0 0 1 1 1V20a1 1 0 0 1-1 1A17 17 0 0 1 3 4a1 1 0 0 1 1-1h3.5a1 1 0 0 1 1 1c0 1.25.2 2.45.57 3.57a1 1 0 0 1-.25 1z"/></svg>
          555-014-27630000
        </li>
        <li>
          <svg viewBox="0 0 24 24"><rect x="2" y="5" width="20" height="14" rx="1" fill="var(--accent)"/><path d="M3 6l9 7 9-7" fill="none" stroke="#fff" stroke-width="1.6"/></svg>
          www.kestrelmechanical.com
        </li>
      </ul>
    </div>
  </section>

</main>
</body>
</html>
```